Orthopedic Arm Surgeon Brochure

Bifold modern design. I will supply the text, my photo, and photos of my textbooks. Prefer colors in the greens, blues, greys. For more information visit LimbForwardClinic.com Please feel free to e-mail me with any questions. Current brochure attached; I want to modernize this, get rid of frames, and change the text.

Target Market(s)

High-end market

Colors
3176b5
33a6d7
33b8a4
abd036
876aae
b768aa

Requirements
Must have
• Beautiful finishes
Should not have
• Bright reds, yellows, oranges that emit fear

```html
<!DOCTYPE html>
<html lang="en">
<head>
<meta charset="utf-8">
<title>Orthopedic Arm Surgeon Brochure</title>
<link rel="stylesheet" href="https://fonts.googleapis.com/css2?family=Open+Sans:wght@400;700&family=Roboto:wght@500;700&family=Roboto+Condensed:wght@400;700&display=swap">
<style>
  :root {
    --paper: #ffffff;
    --backdrop: #e9e7e4;
    --ink: #2b2a29;
    --heading-band: #767270;
    --heading-band-dark: #5f5b59;
    --heading-shadow: #d9d7d5;
    --link-bar: #8c8886;
    --link-box: #6e6a68;
    --accent-gold: #c99a3b;
    --forest: #1e5a2b;
    --forest-deep: #15461f;
    --photo-skin: #e6cbb8;
    --photo-light: #eef0f1;
    --photo-warm: #e8a98f;
  }
  * { box-sizing: border-box; margin: 0; padding: 0; }
  html, body {
    width: 1200px; height: 849px; overflow: hidden;
    background: var(--backdrop);
  }
  .spread {
    position: relative; width: 1200px; height: 849px;
    display: flex;
    font-family: "Open Sans", Arial, sans-serif;
    color: var(--ink);
  }
  .page {
    position: relative; width: 600px; height: 849px;
    background: var(--paper); overflow: hidden;
  }
  .page--right {
    background: linear-gradient(90deg, #e2e1e0 0, #f6f6f6 70px, var(--paper) 160px);
  }
  .section-heading {
    position: absolute; height: 44px;
    display: flex; align-items: center;
    background: linear-gradient(180deg, var(--heading-band) 0%, var(--heading-band-dark) 100%);
    border-radius: 0 22px 22px 0;
    box-shadow: 6px 6px 10px var(--heading-shadow);
    color: #fff;
    font-family: "Roboto", Arial, sans-serif; font-weight: 700; font-size: 19px;
  }
  .section-heading .badge {
    position: absolute; right: 18px; top: 12px;
    width: 20px; height: 20px; border-radius: 50%;
    background: var(--accent-gold); opacity: .85;
  }
  .photo { position: absolute; }
  .body-text {
    position: absolute;
    font-size: 9.4px; line-height: 12.2px; text-align: justify;
  }
  .body-text p + p { margin-top: 12px; }
  .body-text strong { font-weight: 700; }
  .link-bar {
    position: absolute; height: 23px;
    background: var(--link-bar); color: #f4f4f4;
    font-family: "Roboto Condensed", Arial, sans-serif; font-size: 11px;
    display: flex; align-items: center; padding-left: 14px;
  }
  .link-bar strong { font-weight: 700; color: #fff; margin-left: 3px; }
  .link-box {
    position: absolute; background: var(--link-box); color: #f1f1f1;
    font-family: "Roboto Condensed", Arial, sans-serif; font-size: 11px; line-height: 13px;
    padding: 6px 10px;
  }
  .link-box strong { color: #fff; }
  .footer-wave { position: absolute; left: 0; bottom: 0; width: 600px; height: 70px; }
</style>
</head>
<body>
<main class="spread">

  <section class="page page--left">
    <h2 class="section-heading" style="left:0; top:40px; width:328px; padding-left:40px;">Carpal Tunnel Syndrome<span class="badge" aria-hidden="true"></span></h2>

    <div class="photo" role="img" aria-label="Photo of a person holding a sore wrist"
      style="left:35px; top:113px; width:524px; height:143px; background:linear-gradient(90deg, var(--photo-light) 0%, var(--photo-skin) 45%, #f2f2f2 75%, var(--photo-light) 100%);"></div>

    <div class="body-text" style="left:35px; top:262px; width:526px;">
      <p><strong>Carpal Tunnel Syndrome</strong> occurs when the main/median nerve to the handgets pinched at the wrist. This leads to fingers feeling “numb”, “asleep”, “cold”, like they “lack circulation” or have “pins and needles” in them. Carpal tunnel syndrome is usually worst at night or uponawakening. If you wake up at night with your hand numb or painfully asleep, and have to “shake it out” to get relief, you’veprobably got carpal tunnel syndrome. Symptoms alsooften occur with gripping, such as when driving, writing or holding books, cell phones or tools.</p>
      <p>Unless the carpal tunnel syndrome has led to nerve damage, initial treatment often involves splinting the wrist at night when asleep.If that doesn’t work, the carpal tunnel can be released. The least invasive technique is the Single-Incision Endoscopic Carpal Tunnel Release. This quick, minimally invasive, outpatient procedure uses a small incision at the wrist without anyincision in the hand.Compared to other techniques, there is decreased pain anda quicker return to work and other activities. There are no bandages, and hand washing and showering can be performed immediately.</p>
    </div>

    <div class="link-bar" style="left:33px; top:446px; width:528px;">To see a video of an Endoscopic Carpal Tunnel Release please go to: <strong>www.LimbForwardClinic.com</strong></div>

    <h2 class="section-heading" style="left:0; top:491px; width:328px; padding-left:36px;">Cubital Tunnel Syndrome<span class="badge" aria-hidden="true"></span></h2>

    <div class="photo" role="img" aria-label="Photo of a woman holding her elbow with the painful area highlighted"
      style="left:33px; top:560px; width:234px; height:175px; border:1px solid #bdbdbd; background:linear-gradient(90deg, #f3f3f3 0%, var(--photo-skin) 40%, #f5f5f5 65%, var(--photo-warm) 90%, #f3f3f3 100%);"></div>

    <div class="body-text" style="left:278px; top:565px; width:283px;">
      <p><strong>Cubital tunnel syndrome</strong> occurs when the funny bone (ulnar) nerve gets pinched at the elbow. This leads to tingling and numbness of the small finger when the elbow is bent, usually at night or when talking on the phone.Numbness may also occur when the elbows placed on a hard surface.</p>
      <p>Unless nerve damage has occurred, treatment starts with avoiding pressure on the elbow, andnot resting the elbow on desks, arm rests, or other hard objects. Avoid prolonged elbow flexion: use the other hand to hold phones or get a hands-free device.</p>
    </div>

    <div class="link-bar" style="left:33px; top:749px; width:528px;">To see a video of an Endoscopic Cubital Tunnel Release please go to: <strong>www.LimbForwardClinic.com</strong></div>

    <svg class="footer-wave" viewBox="0 0 600 70" preserveAspectRatio="none" aria-hidden="true">
      <path d="M0 20 Q300 8 600 22 L600 70 L0 70 Z" fill="#d8d6d4"/>
      <path d="M0 26 Q300 14 600 28" fill="none" stroke="var(--accent-gold)" stroke-width="2"/>
      <path d="M0 30 Q300 20 600 32 L600 70 L0 70 Z" fill="var(--forest)"/>
      <path d="M0 52 Q300 44 600 54 L600 70 L0 70 Z" fill="var(--forest-deep)"/>
    </svg>
  </section>

  <section class="page page--right">
    <h2 class="section-heading" style="left:0; top:40px; width:374px; padding-left:28px;">Trigger Finger<span class="badge" aria-hidden="true"></span></h2>

    <div class="body-text" style="left:22px; top:118px; width:270px;">
      <p><strong>Trigger finger</strong> occurs when the tendon that moves the finger gets pinched in its tunnel. This causes the finger to get stuck or stiff, which is often worse in the morning. This catching or locking can be quite painful. Grip may also cause pain. The finger may occasionally get stuck straight and be difficult to bend.</p>
      <p>Splinting may temporarily prevent the catching, but doesn’t actually treat the problem.If caught early, a steroid injection can be curative. After 4-6 months the chance of an injection permanently curing the condition is lower, but still often worth a try.</p>
    </div>

    <div class="photo" role="img" aria-label="Photo of a hand holding a stiff bent finger"
      style="left:307px; top:111px; width:244px; height:166px; border:1px solid #9e9e9e; background:linear-gradient(135deg, #efeeed 0%, var(--photo-skin) 50%, #f1efee 100%);"></div>

    <div class="body-text" style="left:25px; top:302px; width:530px;">
      <p>If the triggering returns following an injection, the problem can be definitively treated with a minimally-invasiveTrigger Finger Release. This highly successful outpatient surgery is almost always a permanent cure.</p>
    </div>

    <div class="link-bar" style="left:30px; top:349px; width:526px;">To see a video of an Endoscopic Carpal Tunnel Release please go to: <strong>www.LimbForwardClinic.com</strong></div>

    <h2 class="section-heading" style="left:0; top:398px; width:374px; padding-left:28px;">Wrist Pain<span class="badge" aria-hidden="true"></span></h2>

    <div class="body-text" style="left:25px; top:462px; width:530px;">
      <p>Wrist pain may have many causes and the diagnosis is best made by a fellowship-trained Hand Surgeon. The most common cause is DeQuervain’s tendinitis, which causes pain on the thumb side of the wrist. This occurs when the tendons to the thumb and wrist get pinched in their tunnel. Pain is usually worse with lifting and gripping.</p>
      <p>DeQuervain’s Tendinitis is common in mothers who repetitively lift children. It can also occur following frequent lifting with the thumb up, such as when pulling weeds luggage or moving heavy objects.</p>
      <p>Initial treatment is to avoid lifting with the thumb up. If lifting is necessary, lift with the palm up or the palm down. To lift small children, keep the palm up and ‘scoop under’ the child. Use the other hand to bear most of the weight. A single steroid injection often helps by decreasing inflammation in the tunnel. In mild cases, this can be curative, especially if the problem is treated early and stressful activities can be avoided. Unfortunately, sometimes there’s a very small second tunnel that causes problems and doesn’t respond well to injections.</p>
    </div>

    <svg class="footer-wave" viewBox="0 0 600 70" preserveAspectRatio="none" aria-hidden="true">
      <path d="M0 22 Q300 36 600 18 L600 70 L0 70 Z" fill="#d8d6d4"/>
      <path d="M0 28 Q300 42 600 24" fill="none" stroke="var(--accent-gold)" stroke-width="2"/>
      <path d="M0 32 Q300 46 600 28 L600 70 L0 70 Z" fill="var(--forest)"/>
      <path d="M0 54 Q300 62 600 50 L600 70 L0 70 Z" fill="var(--forest-deep)"/>
    </svg>

    <div class="body-text" style="left:25px; top:665px; width:196px;">
      <p>If the tendinitis recurs after injection, an outpatient tendon release is very effective.To prevent tendon subluxation after tunnel release, I lengthen the restraints that stabilize the tendon and repair them in a lengthened position.</p>
    </div>

    <div class="link-box" style="left:30px; top:747px; width:195px; height:56px;">To see a video of a DeQuervain’s Tendinitis Release please go to: <strong>www.LimbForwardClinic.com</strong></div>

    <div class="photo" role="img" aria-label="Photo of a hand gripping a painful wrist"
      style="left:232px; top:662px; width:368px; height:187px; background:linear-gradient(100deg, rgba(255,255,255,0) 0%, var(--photo-skin) 30%, var(--photo-warm) 55%, var(--photo-skin) 75%, #efe6e0 100%);"></div>
  </section>

</main>
</body>
</html>
```